Kids School Holiday Tennis Camp Flyer

We are a small tennis center based in Sydney's Eastern Suburbs - Australia.
We run coaching programs for kids and adults and also during school holidays organise fun tennis camps for kids aged 6-15 yrs.
Our website is www.rallyburstracquet.com but we dont necessarily need the flyer to tie in with the website design, although happy to have any advice on this.
We would like our logo on there and lots of bright kids colours .... especially yellow's (like tennis balls) and greens (like grass courts).
We would like to convey the message of fun, games, sunshine, interaction but also fitness and learning new tennis skills ..... so its not a play school but a true tennis camp. However - it is also fun to attend and meet other kids.
We would like a double sided flyer if possible with the next terms coaching advertised on the back.
Tennis camp dates to be listed :
Spring Tennis Camps WEEK 1 : Mon Sept 24th - Fri Sept 28th
WEEK 2: Tues Oct 2nd - Fri Oct 5th
Summer Tennis Camps WEEK 1 : Mon Jan 7th - Fri Jan 11th
WEEK 2: Mon Jan 14th - Fri Jan 18th
WEEK 3: Mon Jan 21st - Fri Jan 25th
Flip side of the flyer to advertise kids school term coaching:
Term 4 kids tennis is an 11 week terms, starts Monday October 8th and runs until Friday Dec 21st
Term 1 2013 is also an 11 week term running from Mon Jan 28th to Fri April 12th.
Target Market(s)
Its a kids tennis camp but the parents will be the buyer - so it must have a kids feel but also appeal to the mum and dads !
Industry/Entity Type
Fitness
Look and feel

```html
<!DOCTYPE html>
<html lang="en">
<head>
<meta charset="utf-8">
<title>RallyBurst Tennis Camp – School Holiday Flyer</title>
<link href="https://fonts.googleapis.com/css2?family=Montserrat:wght@800&family=Jost:wght@300;400&display=swap" rel="stylesheet">
<style>
  :root {
    --grass: #86ad48;
    --grass-deep: #5f8a2e;
    --olive: #8d8c6c;
    --ball: #f2c230;
    --ball-light: #f4ec72;
    --white: #ffffff;
    --paper: #ffffff;
  }
  * { box-sizing: border-box; margin: 0; padding: 0; }
  html, body { width: 846px; height: 1200px; overflow: hidden; background: var(--paper); }
  .flyer { position: relative; width: 846px; height: 1200px; overflow: hidden; background: var(--paper); }
  .bands { position: absolute; inset: 0; }

  .intro-bubble {
    position: absolute; left: -30px; top: -80px; width: 510px; height: 510px;
    border-radius: 50%; background: var(--grass); border: 8px solid var(--white);
    box-shadow: 0 3px 8px rgba(0,0,0,.18);
  }
  .intro-text {
    position: absolute; left: 30px; top: 30px; width: 390px;
    transform: rotate(-7deg); text-align: center; color: var(--white);
    font-family: "Montserrat", sans-serif; font-weight: 800;
  }
  .intro-text .lead { font-size: 21px; line-height: 1.25; }
  .intro-text .call { font-size: 36px; line-height: 1.15; margin-top: 4px; }

  .brand {
    position: absolute; left: 498px; top: 68px; display: flex; align-items: center; gap: 14px;
    font-family: "Jost", sans-serif; font-weight: 300; color: var(--grass);
    font-size: 62px; line-height: .88; letter-spacing: -1px;
  }
  .brand-dot { width: 32px; height: 32px; border-radius: 50%; background: var(--ball); flex: none; }

  .camp-photo {
    position: absolute; left: -20px; top: 400px; width: 530px; height: 380px;
    transform: rotate(11deg); border-radius: 32px; border: 8px solid var(--white);
    background: linear-gradient(150deg, #a9c8a0 0%, #6f9a64 45%, #b9b6d8 75%, #4e6f4a 100%);
    box-shadow: 0 3px 8px rgba(0,0,0,.2);
  }

  .hero-ball {
    position: absolute; left: 515px; top: 475px; width: 330px; height: 330px; border-radius: 50%;
    background: radial-gradient(circle at 38% 35%, var(--ball-light) 0%, #e9e24a 55%, #c9c43a 100%);
  }

  .dates-card {
    position: absolute; left: 158px; top: 770px; width: 690px; height: 375px;
    transform: rotate(4deg); border-radius: 28px; background: var(--ball);
    border: 8px solid var(--white); color: var(--white);
    padding: 26px 0 0 44px; box-shadow: 0 3px 8px rgba(0,0,0,.15);
  }
  .dates-title { font-family: "Montserrat", sans-serif; font-weight: 800; font-size: 54px; line-height: 1; letter-spacing: .5px; }
  .season { margin-top: 16px; }
  .season + .season { margin-top: 16px; }
  .season-name { font-family: "Montserrat", sans-serif; font-weight: 800; font-size: 22px; line-height: 1.2; }
  .week { display: flex; font-family: "Jost", sans-serif; font-size: 23px; line-height: 1.25; }
  .week-label { font-weight: 400; width: 104px; }
  .week-range { font-weight: 300; }
</style>
</head>
<body>
<main class="flyer">
  <svg class="bands" width="846" height="1200" viewBox="0 0 846 1200" aria-hidden="true">
    <polygon points="0,440 846,325 846,470 0,585" fill="var(--olive)"/>
    <polygon points="0,650 846,480 846,650 0,820" fill="var(--grass)"/>
    <polygon points="230,1090 846,1090 846,1200 230,1200" fill="var(--grass)"/>
  </svg>

  <div class="intro-bubble"></div>
  <div class="intro-text">
    <p class="lead">Kids,<br>looking to make new<br>friends, learn new<br>tennis skills and have<br>school holiday fun?</p>
    <p class="call">Look no further<br>than RallyBurst<br>Tennis Camp!</p>
  </div>

  <div class="brand">
    <span>rallyburst<br>racquet</span>
    <span class="brand-dot"></span>
  </div>

  <div class="camp-photo" role="img" aria-label="Photo of two smiling children at a tennis net holding up a trophy filled with tennis balls"></div>

  <div class="hero-ball" role="img" aria-label="Large illustrated tennis ball"></div>

  <section class="dates-card">
    <h2 class="dates-title">TENNIS CAMP DATES</h2>
    <div class="season">
      <h3 class="season-name">SPRING TENNIS CAMPS</h3>
      <p class="week"><span class="week-label">WEEK 1</span><span class="week-range">Mon Sept 24th – Fri Sept 28th</span></p>
      <p class="week"><span class="week-label">WEEK 2</span><span class="week-range">Tues Oct 2nd – Fri Oct 5th</span></p>
    </div>
    <div class="season">
      <h3 class="season-name">SUMMER TENNIS CAMPS</h3>
      <p class="week"><span class="week-label">WEEK 1</span><span class="week-range">Mon Jan 7th – Fri Jan 11th</span></p>
      <p class="week"><span class="week-label">WEEK 2</span><span class="week-range">Mon Jan 14th – Fri Jan 18th</span></p>
      <p class="week"><span class="week-label">WEEK 3</span><span class="week-range">Mon Jan 21st – Fri Jan 25th</span></p>
    </div>
  </section>
</main>
</body>
</html>
```